" Atualmente somos dois sócios com experiência no mercado financeiro. A empresa foi fundada em 2016 e desde o início nossos escopo de trabalho se resume a captar clientes para processos de fusões e aquisições, seja para venda parcial ou total das empresas de nossos clientes. Desde a criação da empresa concluímos 3 transações importantes, além de diversas assessorias de valuation (avaliação de valor de empresas) e consultoria financeira. "

```html
<!DOCTYPE html>
<html lang="pt-BR">
<head>
<meta charset="UTF-8">
<title>Vela Capital – Cartões de visita</title>
<link href="https://fonts.googleapis.com/css2?family=Montserrat:wght@400;500;600;700&display=swap" rel="stylesheet">
<style>
  :root {
    --backdrop: #e4e4e6;
    --card: #ffffff;
    --navy: #1c2a3a;
    --gold: #b89a5e;
    --ink: #2a2f36;
    --muted: #4a5058;
  }
  html, body {
    margin: 0;
    padding: 0;
    width: 1200px;
    height: 1200px;
    overflow: hidden;
    background: var(--backdrop);
    font-family: "Montserrat", Arial, sans-serif;
  }
  .sheet {
    position: relative;
    width: 1200px;
    height: 1200px;
  }
  .card {
    position: absolute;
    left: 288px;
    width: 624px;
    height: 240px;
    background: var(--card);
    box-sizing: border-box;
  }
  .card--first { top: 324px; }
  .card--second { top: 636px; }
  .brand {
    position: absolute;
    left: 40px;
    top: 24px;
    display: flex;
    align-items: center;
    gap: 12px;
  }
  .brand__mark {
    width: 34px;
    height: 34px;
    border-radius: 50%;
    background: var(--gold);
  }
  .brand__name {
    font-size: 30px;
    font-weight: 600;
    letter-spacing: 1px;
    color: var(--navy);
    text-transform: uppercase;
  }
  .accent-bar {
    position: absolute;
    left: 4px;
    top: 96px;
    width: 6px;
    height: 144px;
    background: var(--navy);
  }
  .contact {
    position: absolute;
    left: 40px;
    top: 100px;
    color: var(--muted);
    font-size: 12px;
    line-height: 14px;
  }
  .contact__name {
    font-size: 15px;
    font-weight: 700;
    color: var(--ink);
    margin: 0 0 14px;
  }
  .contact__block { margin: 0 0 8px; }
  .contact__social {
    display: flex;
    align-items: center;
    gap: 6px;
    margin-top: 6px;
  }
  .contact__social-dot {
    width: 10px;
    height: 10px;
    border: 1.5px solid var(--gold);
    border-radius: 50%;
    box-sizing: border-box;
  }
</style>
</head>
<body>
<main class="sheet">
  <section class="card card--first">
    <div class="brand">
      <span class="brand__mark"></span>
      <span class="brand__name">Vela Capital</span>
    </div>
    <div class="accent-bar"></div>
    <div class="contact">
      <p class="contact__name">Rafael Moura Tanaka</p>
      <div class="contact__block">
        +55 11 90000-1234<br>
        rafael.tanaka@velacapital.com.br<br>
        www.velacapital.com.br
      </div>
      <div class="contact__block">
        Rua das Acácias, 820 - Cj. 12<br>
        CEP 01234-000 - São Paulo SP
      </div>
      <div class="contact__social"><span class="contact__social-dot"></span>Vela Capital</div>
    </div>
  </section>

  <section class="card card--second">
    <div class="brand">
      <span class="brand__mark"></span>
      <span class="brand__name">Vela Capital</span>
    </div>
    <div class="accent-bar"></div>
    <div class="contact">
      <p class="contact__name">Lucas Ferrante</p>
      <div class="contact__block">
        +55 11 90000-5678<br>
        lucas.ferrante@velacapital.com.br<br>
        www.velacapital.com.br
      </div>
      <div class="contact__block">
        Rua das Acácias, 820 - Cj. 12<br>
        CEP 01234-000 - São Paulo SP
      </div>
      <div class="contact__social"><span class="contact__social-dot"></span>Vela Capital</div>
    </div>
  </section>
</main>
</body>
</html>
```